Flyer-Design für Vertrieb von LED-Beleuchtung
Zielgruppe
Vertrieb von Led Beleuchtung,, für Biergärten
Shop-Adresse lautet www.brilo-nox-markt.de diese sollte auch unbedingt mit rein!
Aufgabenstellung
Es geht Hauptsächlich nur um Bunte Led Birnen und die dazugehörigen Fassungen.
Daher bitte eigene Bilder benutzen und zusätzlich noch welche suchen die passen würden.
Aussagen soll es wie sehr man durch die Umstellung auf unsere Birnen sparen kann und dass sie besser Leuchten als normale und nicht kaputt gehen. 2 alte Flyerversuche von mir selbst liegen bei zwecks preise etc. Die Antwortkarte darf nicht mehr drauf sein da dies bereits Formatprobleme mit der Post gab

```html
<!DOCTYPE html>
<html lang="de">
<head>
<meta charset="utf-8">
<title>Lumivo – Flyer Außen- und Innenseiten</title>
<link rel="stylesheet" href="https://fonts.googleapis.com/css2?family=Oswald:wght@300;400;500;600;700&display=swap">
<style>
  :root {
    --stage: #5a5a5a;
    --yellow: #ebb81a;
    --black: #000000;
    --white: #ffffff;
    --amber: #d9a31c;
    --grey-text: #6b6b6b;
    --label: #f2f2f2;
    --blue: #2f6fc4;
    --green: #58a957;
    --gold: #f2c413;
    --pink: #d6318e;
  }
  * { box-sizing: border-box; margin: 0; padding: 0; }
  html, body { width: 1151px; height: 1200px; overflow: hidden; }
  body {
    background: var(--stage);
    font-family: "Oswald", "Arial Narrow", sans-serif;
    position: relative;
    text-transform: uppercase;
  }
  .spread-label {
    position: absolute;
    left: 202px;
    width: 747px;
    text-align: center;
    color: var(--label);
    font-weight: 300;
    font-size: 22px;
    letter-spacing: 2px;
  }
  .spread {
    position: absolute;
    left: 202px;
    width: 747px;
    height: 528px;
    display: flex;
  }
  .panel { position: relative; height: 100%; overflow: hidden; }
  .panel--yellow { background: var(--yellow); color: var(--black); }
  .panel--black { background: var(--black); color: var(--white); }
  .panel--white { background: var(--white); }
  .abs { position: absolute; }
  .brand {
    font-weight: 700;
    font-size: 22px;
    letter-spacing: 2px;
    line-height: 1;
  }
  .centered { left: 0; right: 0; text-align: center; }

  /* Outside: cover panel with tagline */
  .tagline-small { left: 25px; top: 130px; font-size: 12.5px; line-height: 19.5px; font-weight: 500; }
  .headline-big { left: 25px; top: 282px; font-size: 24px; line-height: 34px; font-weight: 500; color: var(--white); }

  /* Outside: contact panel */
  .consult { top: 94px; font-size: 10.5px; line-height: 20px; font-weight: 300; color: var(--amber); }
  .consult strong { font-weight: 600; color: var(--gold); }
  .contact { top: 400px; font-size: 10px; line-height: 16px; font-weight: 500; }
  .contact .mail { margin-top: 16px; display: block; }

  /* Outside: title panel */
  .cover-photo {
    position: absolute; left: 0; top: 0; width: 100%; height: 389px;
    background:
      radial-gradient(circle at 70% 55%, rgba(220,40,80,0.45), transparent 40%),
      radial-gradient(circle at 35% 20%, rgba(90,110,220,0.45), transparent 45%),
      linear-gradient(160deg, #0b1030 0%, #121a4d 45%, #070a1f 100%);
  }
  .title-sub { left: 25px; top: 444px; font-size: 12.5px; line-height: 19px; font-weight: 500; }
  .title-sub .accent { color: var(--yellow); display: block; }
  .title-sub .muted { color: var(--grey-text); display: block; }

  /* Inside: product image panel */
  .bulbs-image {
    position: absolute; left: 20px; right: 20px; top: 30px; bottom: 30px;
    background: linear-gradient(180deg, #eaf3ea 0%, #f4f4f4 30%, #f6e7f0 55%, #f8f4dc 70%, #e6edf8 100%);
  }

  /* Inside: product details panel */
  .details { left: 30px; right: 20px; top: 56px; }
  .details .product { font-size: 17px; line-height: 25px; font-weight: 500; margin-top: 10px; }
  .details .colours { font-size: 11.5px; font-weight: 600; line-height: 18px; }
  .c-blue { color: var(--blue); } .c-green { color: var(--green); }
  .c-gold { color: var(--gold); } .c-pink { color: var(--pink); }
  .details .spec-title { font-size: 8.5px; font-weight: 600; margin-top: 12px; }
  .details .spec-list { list-style: none; font-size: 8.5px; line-height: 13.5px; font-weight: 600; margin-top: 6px; }
  .features { top: 298px; font-size: 9.5px; line-height: 19px; font-weight: 500; color: #cfcfcf; }
  .features p + p { margin-top: 20px; }

  /* Inside: offer panel */
  .offer { top: 96px; left: 22px; right: 22px; text-align: center; }
  .offer .hook { font-size: 24px; line-height: 34px; font-weight: 500; }
  .offer .sale { font-size: 31px; line-height: 33px; font-weight: 600; color: var(--white); margin-top: 44px; }
  .offer .price-box { border-top: 1px solid #f6d97a; border-bottom: 1px solid #f6d97a; margin-top: 14px; padding: 14px 0 14px; }
  .offer .price { font-size: 26px; line-height: 32px; font-weight: 500; }
  .offer .was { font-size: 20px; line-height: 26px; font-weight: 400; color: var(--grey-text); }
  .offer .was s { text-decoration-thickness: 2px; }
</style>
</head>
<body>

  <h2 class="spread-label" style="top:24px;">Aussenseiten</h2>
  <section class="spread" style="top:64px;" aria-label="Flyer Außenseiten">
    <div class="panel panel--yellow" style="width:244px;">
      <p class="abs brand" style="left:25px; top:96px;">LUMIVO</p>
      <p class="abs tagline-small">Sparen Sie nicht an Personal<br>oder Qualität, sondern<br>an kostenspieliger<br>Aussenbeleuchtung</p>
      <p class="abs headline-big">Viel bewegen<br>durch einfaches<br>austauschen und<br>umsteigen auf<br>umweltschonende<br>LED-Birnen</p>
    </div>
    <div class="panel panel--black" style="width:252px;">
      <p class="abs centered consult">Gerne beraten wir Sie über<br><strong>individuelle Möglichkeiten,</strong><br>Ihren Biergarten<br>perfekt auszuleuchten und<br>neue Akzente zu setzen.</p>
      <p class="abs centered brand" style="top:364px;">LUMIVO</p>
      <p class="abs centered contact">Mark Jelupandor<br>Lindenhofstr. 7<br>72458 Albingen am Hang<span class="mail">Mail: info@lumivo.de</span></p>
    </div>
    <div class="panel panel--white" style="width:251px;">
      <div class="cover-photo" role="img" aria-label="Nachtaufnahme eines Gerüsts mit bunten, leuchtenden Lichterketten in Rot und Blau"></div>
      <p class="abs brand" style="left:25px; top:416px;">LUMIVO</p>
      <p class="abs title-sub"><span class="accent">Stromsparende LED-Beleuchtung</span><span class="muted">für Ihren Biergarten</span></p>
    </div>
  </section>

  <h2 class="spread-label" style="top:614px;">Innenseiten</h2>
  <section class="spread" style="top:654px;" aria-label="Flyer Innenseiten">
    <div class="panel panel--white" style="width:251px;">
      <div class="bulbs-image" role="img" aria-label="Produktfoto: fünf bunte LED-Birnen in Grün, Weiß, Pink, Gelb und Blau mit E27-Fassung"></div>
    </div>
    <div class="panel panel--black" style="width:251px;">
      <div class="abs details">
        <p class="brand">LUMIVO</p>
        <p class="product">LED-Birne 1 Watt<br>in den Farben:</p>
        <p class="colours"><span class="c-blue">Blau</span>, <span class="c-green">Grün</span>, Weiss, <span class="c-gold">Gelb</span>, <span class="c-pink">Pink</span></p>
        <p class="spec-title">Technische Daten</p>
        <ul class="spec-list">
          <li>Fassung E27</li>
          <li>IP65 Spritzwassergeschützt</li>
          <li>7 Lumen bei 6500K</li>
          <li>Verbrauch 1Watt</li>
          <li>Lebensdauer min. 30.000 Stunden</li>
        </ul>
      </div>
      <div class="abs centered features">
        <p>1 Jahr Garantie auf alle Leuchtmittel</p>
        <p>Moderne Spezial-Effekte<br>für Standard-Fassungen</p>
        <p>Umweltschonend durch niedrigen<br>Stromverbrauch von nur 1 Watt und<br>von sehr langer Lebensdauer</p>
        <p>Robustes und stossfestes Material</p>
      </div>
    </div>
    <div class="panel panel--yellow" style="width:245px;">
      <div class="abs offer">
        <p class="hook">Damit Sie nicht<br>im Dunklen sitzen</p>
        <p class="sale">Sommer-Sale<br>Preis</p>
        <div class="price-box">
          <p class="price">2,27 Euro</p>
          <p class="was">statt<br><s>2,78 Euro</s></p>
        </div>
      </div>
    </div>
  </section>

</body>
</html>
```